Billboard design for a new container self storage

I’m after a sign designing for a new container storage opening. located in the heart of Scunthorpe. Open 24/7. Brand new containers. On site security. Best prices guaranteed

Open 24/7
Safe secure self storage
Best prices Guaranteed
Site address
Hollin Row
Scunthorpe
DN17 3QR
Also include next left and an arrow
Dark green/ grey and fluorescent lime green

Contact - info@brindlevaults.co.uk
07924163587

Requirements
Must have
• Instagram logo @Brindleselfstorage

```html
<!DOCTYPE html>
<html lang="en">
<head>
<meta charset="utf-8">
<title>Brindle Self Storage Billboard</title>
<link href="https://fonts.googleapis.com/css2?family=Poppins:ital,wght@0,500;0,600;0,700;0,800;1,800&family=Oswald:wght@500&display=swap" rel="stylesheet">
<style>
  :root {
    --lime: #dcfb3c;
    --forest: #283f22;
    --ink: #1c2a1a;
    --black: #111111;
    --slate: #5a5a5a;
    --white: #ffffff;
    --backdrop-a: #c9c9c9;
    --backdrop-b: #7a7a7a;
  }
  * { margin: 0; padding: 0; box-sizing: border-box; }
  html, body { width: 1052px; height: 1200px; overflow: hidden; }
  body {
    background: linear-gradient(100deg, var(--backdrop-a), var(--backdrop-b));
    font-family: "Poppins", sans-serif;
    position: relative;
  }
  .billboard {
    position: absolute; left: 36px; top: 355px;
    width: 980px; height: 490px;
    box-shadow: 14px 16px 22px rgba(0,0,0,.45);
    overflow: hidden;
  }
  .info-panel { position: absolute; left: 0; top: 0; width: 549px; height: 490px; }
  .band { position: absolute; left: 0; width: 549px; }
  .band--brand { top: 0; height: 146px; background: var(--white); }
  .band--headline { top: 146px; height: 108px; background: var(--lime); }
  .band--features { top: 254px; height: 128px; background: var(--forest); }
  .band--contact { top: 382px; height: 41px; background: linear-gradient(180deg, var(--forest) 0 40%, var(--black) 40%); }
  .band--footer { top: 423px; height: 67px; background: linear-gradient(90deg, var(--black), var(--slate)); }

  .brand { position: absolute; top: 42px; left: 0; width: 549px; display: flex; justify-content: center; align-items: center; gap: 12px; }
  .brand__mark { width: 26px; height: 26px; background: var(--forest); }
  .brand__name { font-weight: 600; font-size: 46px; letter-spacing: 3px; color: var(--ink); line-height: 1; }

  .headline { position: absolute; top: 158px; left: 0; width: 549px; text-align: center;
    font-weight: 800; font-size: 24.5px; line-height: 30px; color: var(--ink); }

  .hours { position: absolute; left: 172px; top: 228px; width: 225px; height: 52px;
    border: 3px solid var(--white); border-radius: 26px; overflow: hidden; display: flex; }
  .hours__days { width: 50%; background: var(--forest); color: var(--white); font-weight: 800; font-size: 24px; display: flex; align-items: center; padding-left: 18px; }
  .hours__open { width: 50%; background: var(--black); color: var(--lime); font-weight: 800; font-style: italic; font-size: 24px; display: flex; align-items: center; padding-left: 30px; }
  .hours__clock { position: absolute; left: 248px; top: 230px; width: 48px; height: 48px; }

  .feature { position: absolute; top: 306px; display: flex; align-items: center; gap: 16px; }
  .feature--storage { left: 55px; }
  .feature--prices { left: 304px; }
  .feature__icon { width: 48px; height: 50px; }
  .feature__text { font-weight: 700; font-size: 17.5px; line-height: 21px; color: var(--white); }
  .feature__text span { color: var(--lime); display: block; }
  .feature-divider { position: absolute; left: 286px; top: 305px; width: 3px; height: 50px; background: var(--lime); }

  .direction { position: absolute; left: 27px; top: 370px; width: 290px; height: 66px; }
  .address { position: absolute; left: 58px; top: 390px; font-family: "Oswald", sans-serif; font-weight: 500;
    font-size: 15px; color: var(--forest); display: flex; align-items: center; gap: 5px; }
  .phone-bar { position: absolute; left: 310px; top: 382px; width: 239px; height: 41px; background: var(--lime); }
  .phone { position: absolute; left: 296px; top: 384px; display: flex; align-items: center; gap: 4px;
    font-weight: 800; font-size: 28.5px; color: var(--black); line-height: 38px; }
  .phone svg { width: 28px; height: 28px; }

  .contacts { position: absolute; left: 64px; top: 446px; display: flex; align-items: center; gap: 8px;
    font-size: 13.5px; font-weight: 500; color: var(--white); }
  .contacts em { font-style: normal; color: var(--lime); }
  .contacts__sep { width: 1px; height: 18px; background: var(--white); margin: 0 2px; }
  .contacts svg { width: 17px; height: 17px; }

  .site-photo { position: absolute; left: 549px; top: 0; width: 431px; height: 490px;
    background: linear-gradient(180deg, #b9cbdc 0%, #d8e2ea 12%, #3d5a55 24%, #2e4743 50%, #405a57 64%, #8c949a 70%, #9aa0a6 100%); }
</style>
</head>
<body>
  <section class="billboard">
    <div class="info-panel">
      <div class="band band--brand"></div>
      <div class="band band--headline"></div>
      <div class="band band--features"></div>
      <div class="band band--contact"></div>
      <div class="band band--footer"></div>

      <div class="brand">
        <span class="brand__mark"></span>
        <span class="brand__name">BRINDLE</span>
      </div>

      <h1 class="headline">Secure self storage container facility<br>in Scunthorpe, Lincolnshire</h1>

      <div class="hours">
        <span class="hours__days">24/7</span>
        <span class="hours__open">OPEN</span>
      </div>
      <svg class="hours__clock" viewBox="0 0 48 48" aria-hidden="true">
        <circle cx="24" cy="24" r="22" fill="#ffffff"/>
        <circle cx="24" cy="24" r="18" fill="#283f22"/>
        <circle cx="24" cy="24" r="14" fill="#e8f1dc"/>
        <path d="M24 14v10l7 4" stroke="#111" stroke-width="2.2" fill="none" stroke-linecap="round"/>
      </svg>

      <div class="feature feature--storage">
        <svg class="feature__icon" viewBox="0 0 48 50" aria-hidden="true">
          <polygon points="24,2 45,13 45,37 24,48 3,37 3,13" fill="#6f8a5c" stroke="#e6ecdc" stroke-width="2.5"/>
          <rect x="13" y="18" width="22" height="15" fill="none" stroke="#fff" stroke-width="2"/>
          <path d="M17 20v11M21 20v11M25 20v11M29 20v11" stroke="#fff" stroke-width="1.5"/>
        </svg>
        <p class="feature__text">SAFE SECURE<span>SELF STORAGE</span></p>
      </div>
      <div class="feature-divider"></div>
      <div class="feature feature--prices">
        <svg class="feature__icon" viewBox="0 0 48 50" aria-hidden="true">
          <polygon points="24,2 45,13 45,37 24,48 3,37 3,13" fill="#6f8a5c" stroke="#e6ecdc" stroke-width="2.5"/>
          <circle cx="24" cy="21" r="8" fill="none" stroke="#fff" stroke-width="2"/>
          <path d="M19 28l-4 9 4-1 2 3 3-7M29 28l4 9-4-1-2 3-3-7" fill="none" stroke="#fff" stroke-width="1.8"/>
        </svg>
        <p class="feature__text">BEST PRICES<span>GUARANTEED</span></p>
      </div>

      <svg class="direction" viewBox="0 0 290 66" aria-hidden="true">
        <polygon points="0,33 30,0 30,12 290,12 290,53 30,53 30,66" fill="#ffffff"/>
      </svg>
      <div class="address">
        <svg width="11" height="14" viewBox="0 0 11 14" aria-hidden="true"><path d="M5.5 0a5.5 5.5 0 0 0-5.5 5.5C0 9.5 5.5 14 5.5 14S11 9.5 11 5.5A5.5 5.5 0 0 0 5.5 0z" fill="#283f22"/><circle cx="5.5" cy="5.5" r="2" fill="#fff"/></svg>
        HOLLIN ROW SCUNTHORPE DN17 3QR
      </div>

      <div class="phone-bar"></div>
      <div class="phone">
        <svg viewBox="0 0 28 28" aria-hidden="true">
          <circle cx="14" cy="14" r="13" fill="#283f22"/>
          <circle cx="14" cy="14" r="10" fill="#dcfb3c"/>
          <path d="M10 8l3 3-2 2c1 2 2 3 4 4l2-2 3 3-2 2c-5 0-10-5-10-10z" fill="#283f22"/>
        </svg>
        07924 163587
      </div>

      <div class="contacts">
        <svg viewBox="0 0 17 17" aria-hidden="true"><rect x="1" y="3" width="15" height="11" fill="#dcfb3c"/><path d="M1 3l7.5 6L16 3" stroke="#111" stroke-width="1.3" fill="none"/></svg>
        <span>info@<em>brindlevaults</em>.co.uk</span>
        <span class="contacts__sep"></span>
        <svg viewBox="0 0 17 17" aria-hidden="true"><circle cx="8.5" cy="8.5" r="7.5" fill="none" stroke="#fff" stroke-width="1.6"/></svg>
        <span><em>@Brindleselfstorage</em></span>
      </div>
    </div>

    <div class="site-photo" role="img" aria-label="Photograph of a row of dark green steel storage containers on a gravel yard under a pale blue sky"></div>
  </section>
</body>
</html>
```